Veterinary Pylon

My veterinary clinic is not clearly visible from the street and I want to place a Pylon next to my driveway. I want a modern, elegant straight Design, the Photo shows the sheduled place. One can see the clinic on our Homepage: www.lindbrook-pet-klinik.at
The last pictures are examples for pylones I like

Target Market(s)

the passing cars often miss my entry...I want to show where to turn left

Colors
3276b5
33a6d7
00a990

Requirements
Must have
• High value, simple elegance, size: 250cm (high) x 100cm (width)
Nice to have
• Our Logo, arrow(?)

A special Text is not necessary but this will be an option:

Biegen sie hier ab und wir biegen es wieder hin!
Should not have
• Too much Color, the colors I have chosen are the possible colors but it‘s not necessary to use them.

```html
<!DOCTYPE html>
<html lang="de">
<head>
<meta charset="utf-8">
<title>Lindbrook Pet Klinik – Pylon</title>
<link rel="stylesheet" href="https://fonts.googleapis.com/css2?family=Open+Sans:wght@600;800&display=swap">
<style>
  :root {
    --navy: #134b91;
    --sky: #33a6d7;
    --teal: #16aa91;
    --white: #ffffff;
  }
  html, body {
    margin: 0;
    padding: 0;
    width: 1200px;
    height: 3000px;
    overflow: hidden;
    background: var(--white);
  }
  .pylon {
    position: relative;
    width: 1200px;
    height: 3000px;
    overflow: hidden;
    background: var(--white);
    font-family: "Open Sans", Arial, sans-serif;
  }
  .pylon__panels {
    position: absolute;
    inset: 0;
  }
  .brand {
    position: absolute;
    left: 90px;
    top: 160px;
    width: 990px;
    height: 260px;
    display: flex;
    align-items: center;
    gap: 48px;
  }
  .brand__dot {
    width: 200px;
    height: 200px;
    border-radius: 50%;
    background: var(--sky);
    flex: none;
  }
  .brand__name {
    margin: 0;
    color: var(--navy);
    font-weight: 800;
    font-size: 112px;
    line-height: 1.02;
    letter-spacing: -1px;
  }
  .turn-arrow {
    position: absolute;
    left: 862px;
    top: 665px;
    width: 238px;
    height: 130px;
  }
  .slogan {
    position: absolute;
    left: 0;
    top: 1515px;
    width: 1132px;
    margin: 0;
    text-align: center;
    color: var(--white);
    font-weight: 600;
    font-size: 96px;
    line-height: 124px;
  }
  .mascot-art {
    position: absolute;
    left: 77px;
    top: 2228px;
    width: 986px;
    height: 583px;
    border-radius: 40px;
    background: linear-gradient(180deg, rgba(255,255,255,0.22), rgba(255,255,255,0.34));
  }
</style>
</head>
<body>
  <main class="pylon">
    <svg class="pylon__panels" width="1200" height="3000" viewBox="0 0 1200 3000" aria-hidden="true">
      <polygon fill="var(--navy)" points="1200,403 1200,3000 0,3000 0,951"/>
      <polygon fill="var(--teal)" points="0,951 471,737 1106,951 1106,2923 0,2923"/>
    </svg>

    <header class="brand">
      <span class="brand__dot"></span>
      <p class="brand__name">Lindbrook<br>Pet Klinik</p>
    </header>

    <svg class="turn-arrow" viewBox="0 0 238 130" aria-label="Pfeil nach links">
      <polygon fill="var(--white)" points="0,65 62,0 100,0 52,50 238,50 238,80 52,80 100,130 62,130"/>
    </svg>

    <p class="slogan">Biegen sie hier ab<br>und wir biegen<br>es wieder hin!</p>

    <div class="mascot-art" role="img" aria-label="Weiße Silhouette von Hund und Katze vor einem Herz mit Herzschlaglinie"></div>
  </main>
</body>
</html>
```